依頼詳細
上記ポータルサイトのWebページデザインを依頼いたします。
両企業のHPをご覧になって企業色をご理解頂き、違和感の無い雰囲気作りを希望いたします。
メインタイトルである「ハルタカグループは子育て支援を応援しています。」は固定でお願いいたします。ロゴマーク等は添付ファイルのものをご利用ください。
尚、添付ファイルはダミーデザインです。このデザインに固執しない自由な発想で結構です。
デザイン作成にあたりスマートホンでの閲覧も考慮頂きたく思います。
サイトURL
http://www.hinata-nestlu.jp
ページ数
1ページ
希望イメージ
シンプル 複雑
単色 カラフル
暗い 明るい
日常 高級
遊び心 厳粛
未来的 伝統的
女性的 男性的
希望する色
赤系、青系、水色系、黄・オレンジ系、同社はブルー・赤・黄色の三色を基本企業色としております。
納品ファイル
• イラストレーター形式 (.ai)
補足説明
子育てに関係するサイトなので、対象となる人物像は20代以降の幅広い年齢層であることをご留意いただきたく思います。
[3/4追記]
いつもお世話になります。本案件につきましてご提案をお考え頂いております方にご案内いたします。ご提案の締切日の変更ではございませんが、クライアントに対して中間報告をしたいと存じます。つきましてはご提案頂ける状態になった方はお早めにご提案頂けましたら幸いでございます。3/12・13と土日も挟みますので、3/10の状況を報告したいと考えております。もちろん3/14の締切は変更ございませんし、早くご提案頂くことでの優遇もございませんが、当方でのプレゼン作業もございますのでご理解頂けましたら幸いでございます。ご無理申し上げますが宜しくお願いいたします。
■ 選んだ理由

この度は本案件に対しまして多数のご提案を頂き誠にありがとうございました。クライアントとの協議の結果pelirund4様のご提案デザインを採用とさせていただきます。選定方法は関連企業を含む100余名の女性によるアンケートを含む審査によります。クライアントのホームページとの親和性も問題なく、女性に好感を持たれる良好なデザインであった考えます。

■ 提案者全員のお礼・コメント

殆どの応募案はどれを採用としても問題が無いほど僅差であり、よく吟味されたデザインであったと思います。残念ながら採用とならなかった応募者の方々にも心から感謝申し上げます。またの機会がございましたら何卒宜しくお願い申し上げます。

```html
<!DOCTYPE html>
<html lang="ja">
<head>
<meta charset="utf-8">
<title>ハルタカ 子育て支援ポータルサイト</title>
<link href="https://fonts.googleapis.com/css2?family=Noto+Sans+JP:wght@400;500;700;900&display=swap" rel="stylesheet">
<style>
:root{
  --page:#efe9dc;
  --page-deep:#e4dccb;
  --white:#ffffff;
  --ink:#4a3f35;
  --muted:#7a6e62;
  --brand-red:#d9412f;
  --brand-blue:#1f5fa8;
  --card-line:#ddd4c4;
  --photo-top:#f3ede4;
  --photo-bottom:#c9b9a4;
  --footer:#dcd2bf;
}
*{box-sizing:border-box;margin:0;padding:0}
html,body{width:861px;height:1200px;overflow:hidden}
body{
  background:linear-gradient(var(--page),var(--page-deep));
  font-family:"Noto Sans JP",sans-serif;color:var(--ink);
  position:relative;
}
.site-header{
  height:58px;background:var(--white);
  display:flex;align-items:center;justify-content:center;gap:8px;
  border-bottom:1px solid var(--card-line);
}
.site-header .mark{width:14px;height:14px;background:var(--brand-red)}
.site-header .brand{font-size:18px;font-weight:700;color:var(--brand-red);letter-spacing:1px}
.hero{
  position:relative;height:372px;
  background:linear-gradient(180deg,var(--photo-top) 0%,#e9ddcf 45%,var(--photo-bottom) 100%);
}
.hero-title{
  position:absolute;top:34px;left:0;right:0;text-align:center;
  font-weight:900;color:var(--ink);font-size:34px;line-height:1.3;letter-spacing:2px;
}
.hero-title .accent{color:var(--brand-red)}
.partners{
  position:absolute;top:458px;left:80px;
  display:grid;grid-template-columns:336px 336px;column-gap:30px;row-gap:22px;
}
.partner-card{
  background:var(--white);border:1px solid var(--card-line);height:132px;padding:14px 16px;
}
.partner-card .badge{
  display:block;margin:0 auto 12px;width:160px;height:40px;border-radius:6px;
}
.partner-card p{font-size:10.5px;line-height:1.6;color:var(--muted)}
.b1{background:#f6c8a0}.b2{background:#f3d0da}.b3{background:#bcd3ee}
.b4{background:#f7e08a}.b5{background:#f2b9a8}.b6{background:#a9d4ef}
.group-links{
  position:absolute;top:946px;left:80px;display:flex;gap:30px;
}
.group-link{
  width:336px;height:62px;background:var(--white);border:1px solid var(--card-line);
  display:flex;align-items:center;justify-content:center;gap:10px;
  font-size:19px;font-weight:700;color:var(--brand-blue);
}
.group-link .mark{width:14px;height:14px;background:var(--brand-blue)}
.to-top{
  position:absolute;top:1030px;right:80px;font-size:10px;color:var(--muted);
  display:flex;align-items:center;gap:4px;
}
.site-footer{
  position:absolute;top:1056px;left:0;right:0;height:110px;background:var(--footer);
  padding:16px 80px;display:flex;justify-content:space-between;
}
.footer-nav{list-style:none;font-size:10px;color:var(--ink);line-height:2}
.footer-nav li::before{content:"▸ ";color:var(--brand-blue)}
.company{font-size:9.5px;line-height:1.7;color:var(--ink);display:flex;gap:14px;width:360px}
.company .name{font-weight:700;white-space:nowrap}
.copyright{position:absolute;bottom:14px;left:0;right:0;text-align:center;font-size:9px;color:var(--muted)}
</style>
</head>
<body>
<header class="site-header">
  <span class="mark"></span>
  <span class="brand">ハルタカ 子育て支援ポータルサイト</span>
</header>

<section class="hero" role="img" aria-label="床に寝そべって笑顔で並ぶ三世代の家族の写真">
  <h1 class="hero-title">ハルタカグループは<br><span class="accent">「子育て支援」</span>を応援しています。</h1>
</section>

<section class="partners">
  <article class="partner-card"><span class="badge b1"></span><p>こちらにはパートナーサイト紹介のテキストが入ります。どういったサイトで、どんな内容を掲載しているかの紹介文が入ります。</p></article>
  <article class="partner-card"><span class="badge b2"></span><p>こちらにはパートナーサイト紹介のテキストが入ります。どういったサイトで、どんな内容を掲載しているかの紹介文が入ります。</p></article>
  <article class="partner-card"><span class="badge b3"></span><p>こちらにはパートナーサイト紹介のテキストが入ります。どういったサイトで、どんな内容を掲載しているかの紹介文が入ります。</p></article>
  <article class="partner-card"><span class="badge b4"></span><p>こちらにはパートナーサイト紹介のテキストが入ります。どういったサイトで、どんな内容を掲載しているかの紹介文が入ります。</p></article>
  <article class="partner-card"><span class="badge b5"></span><p>こちらにはパートナーサイト紹介のテキストが入ります。どういったサイトで、どんな内容を掲載しているかの紹介文が入ります。</p></article>
  <article class="partner-card"><span class="badge b6"></span><p>こちらにはパートナーサイト紹介のテキストが入ります。どういったサイトで、どんな内容を掲載しているかの紹介文が入ります。</p></article>
</section>

<nav class="group-links">
  <a class="group-link"><span class="mark"></span>ハルタカホールディングス</a>
  <a class="group-link"><span class="mark"></span>東嶺運輸</a>
</nav>

<a class="to-top"><svg width="10" height="10" viewBox="0 0 10 10"><path d="M1 7 L5 3 L9 7" fill="none" stroke="#1f5fa8" stroke-width="1.6"/></svg>ページの先頭へ</a>

<footer class="site-footer">
  <ul class="footer-nav">
    <li>プライバシーポリシー</li>
    <li>リンクポリシー</li>
    <li>免責事項</li>
  </ul>
  <div class="company">
    <span class="name">運営会社「子育て支援」</span>
    <span>〒503-0000 岐阜県大垣市中町1-1<br>TEL 0584-00-0000<br>FAX 0584-00-0001<br>E-mail info@harutaka-nest.jp</span>
  </div>
</footer>
<p class="copyright">Copyright © 2016 harutaka-nest. All Rights Reserved.</p>
</body>
</html>
```